Poetry Book Cover Design Project

Looking for a minimalistic book cover design for a collection of poems. The book title is "Before The Morning Turns To Glass". There are three parts to the book. First covers poetry in the theme of Rage. Second love and desire. The third is strange poems. Essentially the sections are "Rage", "Desire" and the "Strange". The reason for the title "Before The Morning Turns To Glass" is as if someone is writing these till life changes towards the intended outcome as felt in each poem. I want to have the author's name "Nirosha Kulathunge" at the bottom. Ilustration attached.
- Minimalistic

```html
<!DOCTYPE html>
<html lang="en">
<head>
<meta charset="utf-8">
<title>Before The Morning Turns To Glass – Cover Wrap</title>
<link href="https://fonts.googleapis.com/css2?family=Marcellus&family=Pinyon+Script&display=swap" rel="stylesheet">
<style>
  :root {
    --page: #c9d0d3;
    --blue: #0b4aa6;
    --blue-deep: #083b8e;
    --navy: #0a2a66;
    --orange: #ff7f00;
    --red: #b51a00;
    --paper: #ffffff;
    --ice: #b9d2f2;
    --silver-hi: #ffffff;
    --silver-lo: #9fb0c4;
    --script-blue: #5f8fd8;
  }
  html, body {
    margin: 0;
    padding: 0;
    width: 960px;
    height: 1200px;
    overflow: hidden;
    background: var(--page);
  }
  .canvas {
    position: relative;
    width: 960px;
    height: 1200px;
  }
  .cover-wrap {
    position: absolute;
    left: 20px;
    top: 275px;
    width: 920px;
    height: 650px;
    overflow: hidden;
    box-shadow: 0 6px 18px rgba(0,0,0,.25);
  }
  .cover-art {
    position: absolute;
    inset: 0;
    width: 920px;
    height: 650px;
  }
  .portrait-area {
    position: absolute;
    left: 0;
    top: 22px;
    width: 175px;
    height: 395px;
    background: linear-gradient(90deg, var(--navy) 0%, #0c3a85 75%, rgba(11,74,166,0) 100%);
    opacity: .85;
  }

  /* Back cover */
  .back {
    position: absolute;
    left: 170px;
    top: 0;
    width: 255px;
    height: 420px;
    color: var(--paper);
    font-family: "Marcellus", serif;
    text-align: center;
  }
  .back-author {
    margin: 52px 0 16px;
    font-size: 12px;
    letter-spacing: .3px;
  }
  .back-blurb p {
    margin: 0 0 9px;
    font-size: 8.2px;
    line-height: 10.8px;
    text-transform: uppercase;
  }

  /* Spine */
  .spine {
    position: absolute;
    left: 439px;
    top: 0;
    width: 34px;
    height: 650px;
    font-family: "Marcellus", serif;
    color: var(--paper);
  }
  .spine-title, .spine-author {
    position: absolute;
    left: 50%;
    writing-mode: vertical-rl;
    transform: translateX(-50%);
    white-space: nowrap;
  }
  .spine-title {
    top: 36px;
    font-size: 17px;
    letter-spacing: .2px;
  }
  .spine-author {
    top: 465px;
    font-size: 10px;
  }

  /* Front cover */
  .front {
    position: absolute;
    left: 473px;
    top: 0;
    width: 447px;
    height: 650px;
    text-align: center;
    font-family: "Marcellus", serif;
  }
  .series-label {
    position: absolute;
    top: 54px;
    width: 100%;
    font-size: 17px;
    letter-spacing: 8px;
    color: var(--ice);
  }
  .title {
    position: absolute;
    top: 112px;
    width: 100%;
    margin: 0;
    font-weight: normal;
  }
  .title span { display: block; }
  .title-script {
    font-family: "Pinyon Script", cursive;
    font-size: 50px;
    line-height: 48px;
    color: var(--script-blue);
    text-shadow: 1px 1px 0 rgba(255,255,255,.35), 0 2px 4px rgba(0,0,0,.3);
  }
  .title-caps {
    font-family: "Marcellus", serif;
    line-height: 70px;
    background: linear-gradient(180deg, var(--silver-hi) 0%, var(--silver-lo) 55%, var(--silver-hi) 100%);
    -webkit-background-clip: text;
    background-clip: text;
    color: transparent;
    filter: drop-shadow(1px 2px 2px rgba(0,0,0,.45));
  }
  .title-caps.is-long { font-size: 66px; }
  .title-caps.is-short { font-size: 82px; }
  .front-author {
    position: absolute;
    top: 588px;
    width: 100%;
    font-size: 13px;
    color: var(--paper);
  }
</style>
</head>
<body>
<main class="canvas">
  <section class="cover-wrap">
    <svg class="cover-art" viewBox="0 0 920 650" aria-hidden="true">
      <defs>
        <linearGradient id="sky" x1="0" y1="0" x2="0" y2="1">
          <stop offset="0" stop-color="#0b4aa6"/>
          <stop offset="1" stop-color="#083b8e"/>
        </linearGradient>
        <radialGradient id="ember" cx="0.5" cy="0.55" r="0.75">
          <stop offset="0" stop-color="#ff8200"/>
          <stop offset="0.6" stop-color="#ff6a00"/>
          <stop offset="1" stop-color="#b51a00"/>
        </radialGradient>
      </defs>
      <rect width="920" height="650" fill="url(#sky)"/>
      <path d="M0 416 L60 410 L120 404 L180 398 L230 400 L270 404 L330 406 L390 414 L440 428 L500 446 L560 458 L620 466 L680 476 L740 486 L800 496 L860 508 L920 520 L920 650 L0 650 Z" fill="url(#ember)"/>
      <path d="M0 416 L14 412 L22 415 L36 410 L50 413 L62 408 L78 411 L92 405 L108 408 L120 402 L136 405 L150 399 L166 402 L180 396 L196 399 L210 396 L230 398 L246 401 L262 399 L280 404 L298 402 L316 405 L334 404 L350 408 L368 407 L388 412 L402 414 L420 420 L440 426 L456 433 L474 437 L492 443 L510 446 L528 451 L546 453 L562 457 L580 458 L598 463 L616 464 L634 469 L652 470 L670 475 L688 476 L706 481 L724 482 L742 487 L760 489 L778 493 L796 495 L814 500 L832 502 L850 507 L868 509 L886 513 L904 515 L920 519 L920 526 L900 522 L880 519 L860 515 L840 512 L820 507 L800 504 L780 499 L760 496 L740 492 L720 489 L700 485 L680 482 L660 477 L640 474 L620 470 L600 468 L580 464 L560 462 L540 458 L520 455 L500 451 L480 446 L460 440 L440 433 L420 426 L400 420 L380 418 L360 413 L340 411 L320 410 L300 407 L280 409 L260 405 L240 406 L220 403 L200 405 L180 402 L160 407 L140 408 L120 410 L100 413 L80 415 L60 417 L40 418 L20 421 L0 422 Z" fill="#ffffff"/>
    </svg>

    <div class="portrait-area" role="img" aria-label="Blue-toned side profile photograph of a man facing right"></div>

    <article class="back">
      <div class="back-author">NIROSHA KULATHUNGE</div>
      <div class="back-blurb">
        <p>Lorem ipsum dolor sit amet, rebum verterem tacimates cu nec, eum zril docendi accusata ex. Agam laoreet usu ex, libris posidonium est ei. Ei voluptaria deterruisset eos, eu usu exerci splendide. Eu eum tritani assueverit, ex eos tritani detraxit. Ei eam dicta tritani et decore consul virtute per.</p>
        <p>Nam eu summo definitiones, eu eruditi praesent mel, ad est iriure honestatis. At mel consul instructior. Usu mediocrem theophrastus an, ea vide delicata necessitatibus pro. Sit possit probatus consulatu ut, ei elit intellegam ius.</p>
        <p>Vim quem accumsan tincidunt ea, ad vim mutat inermis. Illum discere his ad, mel ex error prompta aliquid. Mei vocent corrumpit assueverit ad. Minim quodsi docendi usu ad, has habeo illud consequat no. Mei et amet commodo, in menandri contentiones duo.</p>
        <p>Pri in dicunt phaedrum, in pro modo agam. Ad duo autem ullum summo, in wisi choro cum. Eam oratio noluisse cu, mel doming indoctum ea. Alterum interesset nam an, id hinc tollit labore per. Qui te illum accusamus, eu malis cetero facilisi nam, ridens propriae qui ea.</p>
      </div>
    </article>

    <aside class="spine">
      <div class="spine-title">BEFORE THE MORNING TURNS TO GLASS</div>
      <div class="spine-author">NIROSHA KULATHUNGE</div>
    </aside>

    <article class="front">
      <div class="series-label">POETRY BOOK</div>
      <h1 class="title">
        <span class="title-script">Before The</span>
        <span class="title-caps is-long">MORNING</span>
        <span class="title-script">Turns To</span>
        <span class="title-caps is-short">GLASS</span>
      </h1>
      <div class="front-author">NIROSHA KULATHUNGE</div>
    </article>
  </section>
</main>
</body>
</html>
```